Business card design for global fintech startup

Veltrix is a modern payments platform for the global insurance industry, serving international health, life, and travel insurers, MGAs, brokers, and partners.

We need a professional, premium business card for use at insurance conferences and executive meetings. The goal is to create a card that feels trustworthy, modern, and high-quality, while still being distinctive and memorable in a stack of business cards.

Target audience:
Senior insurance executives (VP, C-suite).

Design goals:
Clear, professional, and credible
Modern but not trendy
Premium and well-structured
Easy to read and practical for networking

Brand direction:
Brand-first (company over individual)
Follow existing brand guidelines where possible
Clean layout, strong hierarchy, excellent readability

Must include:
Name
Title
Company name (Veltrix)
Logo
Email
Phone/Whatsapp
Website (www.withveltrix.example)
Tagline - Clear Paths For Payment

Materials & finish:
Open to designer recommendations for premium look and feel.

Please avoid:
Flashy or trendy startup styles
Generic insurance icons or clichés
Cluttered layouts or hard-to-read text

Deliverables:
Front and back business card, print-ready files.

Target Market(s)

Global Insurance executives

Industry/Entity Type

Fintech, Insurtech, Insurance, Financial Services

Contact Information for Business Card

Name Title Company name (Veltrix) Logo Email Phone/Whatsapp Website (www.withveltrix.example) Tagline - Clear Paths For Payment

Font styles to use
Other font styles liked:
• See brand guidelines

Requirements
Nice to have
• something that stands out/makes us more memorable while still remaining professional
Should not have
• Please avoid: Flashy or trendy startup styles Generic insurance icons or clichés Cluttered layouts or hard-to-read text

```html
<!DOCTYPE html>
<html lang="en">
<head>
<meta charset="utf-8">
<title>Veltrix Business Card</title>
<link href="https://fonts.googleapis.com/css2?family=Montserrat:wght@500;600&family=Arimo:wght@400&display=swap" rel="stylesheet">
<style>
  :root{
    --bg:#4a4a4a;
    --card:#232323;
    --white:#ffffff;
    --cyan:#19c9f2;
    --gold:#f3c26a;
    --orange:#ff7e14;
    --violet:#7417e6;
    --blue:#1e90f0;
    --sand:#f6c86e;
  }
  *{margin:0;padding:0;box-sizing:border-box}
  html,body{width:1200px;height:800px;overflow:hidden;background:var(--bg)}
  .stage{position:relative;width:1200px;height:800px}
  .card{position:absolute;left:300px;width:600px;height:342px;background:var(--card);border-radius:18px;overflow:hidden;box-shadow:0 10px 24px rgba(0,0,0,.35)}
  .card--front{top:40px}
  .card--back{top:418px}

  .brand{position:absolute;display:flex;align-items:center;gap:14px;font-family:"Montserrat",sans-serif;font-weight:500;color:var(--white);letter-spacing:.12em}
  .brand__dot{width:14px;height:14px;border-radius:50%;background:var(--cyan)}
  .card--front .brand{left:44px;top:52px;font-size:30px}

  .brand-panel{position:absolute;right:0;top:0;width:210px;height:342px;background:linear-gradient(160deg,var(--violet) 0%,var(--blue) 35%,var(--orange) 70%,var(--sand) 100%);border-left:6px solid var(--white)}

  .person{position:absolute;left:44px;top:166px}
  .person__name{font-family:"Montserrat",sans-serif;font-weight:600;font-size:24px;letter-spacing:.04em;color:var(--cyan);text-transform:uppercase}
  .person__title{font-family:"Arimo",sans-serif;font-size:15px;color:var(--white);margin-top:2px}

  .contacts{position:absolute;left:44px;top:238px;list-style:none;font-family:"Arimo",sans-serif;font-size:15px;color:var(--white)}
  .contacts li{display:flex;align-items:center;gap:8px;height:24px}
  .contacts svg{width:16px;height:16px;fill:none;stroke:var(--gold);stroke-width:2}

  .card--back .brand{left:0;right:0;top:108px;justify-content:center;font-size:40px}
  .tagline{position:absolute;left:0;right:0;top:196px;display:flex;align-items:center;gap:14px;padding:0 34px;font-family:"Montserrat",sans-serif;font-weight:600;font-size:22px;color:var(--white);white-space:nowrap}
  .tagline__rule{flex:1;height:5px;border-top:1px solid var(--white);border-bottom:1px solid var(--white)}
</style>
</head>
<body>
<main class="stage">
  <section class="card card--front" aria-label="Card front">
    <div class="brand"><span class="brand__dot"></span>VELTRIX</div>
    <div class="person">
      <p class="person__name">Daniel Reyes</p>
      <p class="person__title">Managing Director</p>
    </div>
    <ul class="contacts">
      <li><svg viewBox="0 0 16 16"><path d="M4 2l2 3-1.5 1.5a8 8 0 0 0 5 5L11 10l3 2-1.5 2.5C7 14 2 9 1.5 3.5z"/></svg>044-555 010 200</li>
      <li><svg viewBox="0 0 16 16"><rect x="1.5" y="3.5" width="13" height="9"/><path d="M1.5 3.5l6.5 5 6.5-5"/></svg>info@veltrix.example</li>
      <li><svg viewBox="0 0 16 16"><circle cx="8" cy="8" r="6.5"/><path d="M1.5 8h13M8 1.5c3 3.5 3 9.5 0 13M8 1.5c-3 3.5-3 9.5 0 13"/></svg>www.withveltrix.example</li>
    </ul>
    <div class="brand-panel" role="img" aria-label="Large brand graphic in violet, blue, orange and sand tones"></div>
  </section>

  <section class="card card--back" aria-label="Card back">
    <div class="brand"><span class="brand__dot"></span>VELTRIX</div>
    <p class="tagline"><span class="tagline__rule"></span>Clear Paths For Payment<span class="tagline__rule"></span></p>
  </section>
</main>
</body>
</html>
```